Holistic/ Sports Psychologist needs flyer design

I need a flyer designed that catches the attention of potential customers - (parents of young athletes and athletes) who may be looking for psychological services. I have a logo and all the relevant info for the flyer but would like someone to take it and make it look creative, fun, fresh and attention getting for high school and college athletes. The colors used can be from my logo design which represents my holistic approach.
Target Market(s)
high school and collegiate athletes
Industry/Entity Type
sports psychology
Requirements
Must have
- Info I put on the flyer with my logo and please add some graphics and color based on my logo

```html
<!DOCTYPE html>
<html lang="en">
<head>
<meta charset="utf-8">
<title>Holistic Psychology Flyer</title>
<link href="https://fonts.googleapis.com/css2?family=Outfit:wght@400;500;600;700;800&display=swap" rel="stylesheet">
<style>
  :root {
    --blue: #3f6597;
    --green: #9cc36b;
    --green-soft: #cfe2b5;
    --panel: #e3eaee;
    --ink: #333638;
    --lilac: #b7b2d9;
    --white: #ffffff;
  }
  * { margin: 0; padding: 0; box-sizing: border-box; }
  html, body { width: 989px; height: 1200px; overflow: hidden; background: var(--white); }
  body { font-family: "Outfit", sans-serif; color: var(--ink); }
  .flyer { position: relative; width: 989px; height: 1200px; overflow: hidden;
    background: linear-gradient(180deg, #ffffff 0%, #f3f4f5 40%); }

  .corner-blob { position: absolute; top: -60px; right: -40px; width: 260px; height: 230px;
    border-radius: 50%; background: var(--green-soft); opacity: .8; }
  .corner-blob.small { top: 120px; right: -70px; width: 150px; height: 150px; background: var(--green); opacity: .55; }

  .brand { position: absolute; left: 60px; top: 40px; display: flex; align-items: center; z-index: 2; }
  .brand-mark { width: 150px; height: 150px; border-radius: 50%; background: var(--blue);
    border: 8px solid #dfe6ef; flex: none; }
  .brand-name { position: relative; margin-left: 22px; padding-bottom: 8px; }
  .brand-name span { position: relative; z-index: 1; font-size: 38px; font-weight: 500;
    color: var(--blue); letter-spacing: .5px; }
  .brand-name::after { content: ""; position: absolute; left: -10px; right: -70px; bottom: -30px;
    height: 32px; background: var(--green); }

  .telehealth { position: absolute; right: 58px; top: 230px; display: flex; align-items: center; gap: 12px; z-index: 2; }
  .telehealth-text small { display: block; font-size: 18px; line-height: 1; color: var(--ink); }
  .telehealth-text strong { display: block; font-size: 44px; font-weight: 800; line-height: 1; color: var(--ink); }

  .sessions { position: absolute; right: 58px; top: 352px; display: flex; align-items: center; gap: 10px; text-align: right; z-index: 2; }
  .sessions p { font-size: 16px; line-height: 1.15; }
  .sessions b { font-weight: 700; font-size: 18px; }

  .services-panel { position: absolute; left: 0; right: 0; top: 525px; bottom: 0; background: var(--panel); }
  .panel-swirl { position: absolute; right: -30px; top: 690px; width: 210px; height: 130px;
    border: 22px solid var(--lilac); border-radius: 50%; opacity: .35; }

  .headline { position: absolute; left: 70px; top: 300px; z-index: 2; }
  .headline h1 { font-size: 84px; font-weight: 800; line-height: .92; color: var(--blue); letter-spacing: -1px; }
  .headline h2 { margin-top: 8px; font-size: 30px; font-weight: 700; line-height: 1.2; color: var(--blue); }

  .services { position: absolute; left: 70px; right: 58px; top: 543px; z-index: 2; }
  .services h3 { font-size: 27px; font-weight: 600; line-height: 1.15; color: var(--ink); margin-bottom: 14px; }
  .service { position: relative; padding-left: 22px; margin-bottom: 10px; }
  .service::before { content: ""; position: absolute; left: 2px; top: 5px; width: 4px; height: 14px;
    background: var(--blue); transform: skewX(-35deg); }
  .service h4 { font-size: 15px; font-weight: 700; text-transform: uppercase; line-height: 1.2; }
  .service p { font-size: 14px; line-height: 1.28; }

  .footer-wave { position: absolute; left: 0; top: 0; width: 989px; height: 1200px; }

  .background { position: absolute; left: 70px; top: 900px; width: 560px; z-index: 2; }
  .background-tag { display: flex; align-items: stretch; height: 34px; margin-bottom: 10px; }
  .background-tag::before { content: ""; width: 34px; background: var(--green);
    clip-path: polygon(40% 0, 100% 0, 100% 100%, 0 100%); }
  .background-tag span { background: var(--blue); color: var(--white); font-size: 21px; font-weight: 600;
    padding: 0 18px 0 10px; line-height: 34px; }
  .background p { font-size: 14px; line-height: 1.3; margin-bottom: 9px; }
  .background b { font-weight: 700; }

  .address { position: absolute; left: 70px; top: 1133px; color: var(--white); font-size: 24px;
    font-weight: 600; line-height: 1.15; font-style: normal; z-index: 2; }
  .contact { position: absolute; right: 58px; top: 1088px; color: var(--white); text-align: right; z-index: 2; }
  .contact .web { font-size: 15px; letter-spacing: 2px; }
  .contact .phone { display: flex; align-items: center; justify-content: flex-end; gap: 8px;
    font-size: 30px; font-weight: 700; margin-top: 4px; }
</style>
</head>
<body>
<main class="flyer">
  <div class="corner-blob"></div>
  <div class="corner-blob small"></div>

  <div class="services-panel"></div>
  <div class="panel-swirl"></div>

  <svg class="footer-wave" viewBox="0 0 989 1200" aria-hidden="true">
    <path d="M0 1110C400 1110 760 1085 989 1010V1200H0Z" fill="#9cc36b"/>
    <path d="M0 1122C400 1122 760 1100 989 1030V1200H0Z" fill="#3f6597"/>
    <circle cx="40" cy="1160" r="34" fill="none" stroke="#5b7fae" stroke-width="12" opacity=".6"/>
    <circle cx="150" cy="1195" r="30" fill="none" stroke="#5b7fae" stroke-width="12" opacity=".6"/>
  </svg>

  <header class="brand">
    <div class="brand-mark"></div>
    <div class="brand-name"><span>Dr. Rosalind Averhart</span></div>
  </header>

  <div class="telehealth">
    <svg width="76" height="68" viewBox="0 0 76 68" aria-hidden="true">
      <rect x="3" y="3" width="70" height="48" rx="4" fill="none" stroke="#333638" stroke-width="5"/>
      <path d="M30 60h16M38 51v9" stroke="#333638" stroke-width="5" stroke-linecap="round"/>
      <path d="M38 44c-10-7-15-12-15-18a7 7 0 0 1 15-3 7 7 0 0 1 15 3c0 6-5 11-15 18z" fill="none" stroke="#333638" stroke-width="3.5"/>
      <path d="M12 28h14l4-7 5 13 4-8h25" fill="none" stroke="#333638" stroke-width="3"/>
    </svg>
    <div class="telehealth-text">
      <small>All services are provided<br>online via</small>
      <strong>telehealth</strong>
    </div>
  </div>

  <div class="sessions">
    <p>Sessions are<br><b>30 or 55 minutes</b></p>
    <svg width="36" height="42" viewBox="0 0 36 42" aria-hidden="true">
      <rect x="13" y="1" width="10" height="5" fill="#333638"/>
      <circle cx="18" cy="24" r="15" fill="none" stroke="#333638" stroke-width="4"/>
      <path d="M18 24V14A10 10 0 1 1 8 24z" fill="#333638"/>
    </svg>
  </div>

  <section class="headline">
    <h1>Holistic<br>Psychology</h1>
    <h2>and sports Psychology Consulting</h2>
  </section>

  <section class="services">
    <h3>Ways to Improve Athletic Performance Using Sports and<br>Holistic Psychology</h3>
    <div class="service">
      <h4>Mental Skills Training</h4>
      <p>Ex: visualization, goal-setting, motivation, self- talk, mindset, concentration techniques.</p>
    </div>
    <div class="service">
      <h4>Performance Enhancement</h4>
      <p>Eliminate psychological barriers that are hindering performance such as self- doubt, perfectionism, fear of failure, and burnout.</p>
    </div>
    <div class="service">
      <h4>Mental Health</h4>
      <p>Anxiety and stress management by using relaxation techniques, breathwork, and mindfulness practices.</p>
    </div>
    <div class="service">
      <h4>Injury Recovery Support</h4>
      <p>Assist athletes in maintaining resilience and positive mental attitude during rehabilitation as well as processing emotions relating to any potential trauma caused by the injury or life transitions resulting from it.</p>
    </div>
    <div class="service">
      <h4>Burnout Prevention</h4>
      <p>Teach athletes how to have balance in sports and life so they can experience longevity in their sports as well as overall optimal health and well-being.</p>
    </div>
  </section>

  <section class="background">
    <div class="background-tag"><span>Background</span></div>
    <p><b>Dr. Rosalind Averhart</b> is a licensed psychologist. She understands the unique experiences of athletes due to her background as an All-American swimmer, collegiate and age group swim coach, parent of a collegiate/professional athlete, and sports psychology researcher. She works with athletes to optimize performance and overall well-being.</p>
    <p>Her specializations include: performance anxiety, mental performance, stress management, anxiety, depressions, trauma, life transitions, relationship issues, injury, and sleep.</p>
  </section>

  <address class="address">2280 Tidewater Lane #310<br>Harbor Point, FL 32099</address>

  <div class="contact">
    <div class="web">drrosalindaverhart.com</div>
    <div class="phone">
      <svg width="16" height="26" viewBox="0 0 16 26" aria-hidden="true">
        <rect x="1.5" y="1.5" width="13" height="23" rx="2.5" fill="none" stroke="#9cc36b" stroke-width="2.5"/>
        <path d="M6 21h4" stroke="#9cc36b" stroke-width="2"/>
      </svg>
      <span>555-017-4829</span>
    </div>
  </div>
</main>
</body>
</html>
```